Professional Lawn Treatment flyer (double sided) needed for established gardening company

We are an established and trusted gardening company in Swindon, UK, and are about to launch a new Lawn Treatment Service. This will be marketed to both existing and new customers and needs to reflect our current professional image. The flyer will need to be double-sided, portrait orientation and correctly sized so to be printed on A5.

If you look on our website www.tavistrowgardening.co.uk, you will see our colours are purple and green. We would like you to use these exact shades of purple and green in your design.

As part of the design, we will need you to put together an infographic table to show our packages. I have attached a spreadsheet which explains these packages but I will need you to create a visually appealing table that fits in with the overall design of the flyer. I don't want you to simply cut and paste my basic table into the design.

In terms of what needs to be included, I have tried to be as specific as possible here but please feel free to message me if you need any further information or clarification.

FRONT SIDE:
The title of our service is:
Expert Lawn Treatment Service

Our strapline will need to be included somewhere:
"Lawn care by your local gardening expert"

The front side of the flyer will need to contain our logo - different versions of which can be found within my dropbox folder here...

https://www.sharebinnu.co.uk/sh/k7qd21mzplax/QRT8xWbnNeLu4Pa-ZxYyhKcLo?dl=0

The front side will need to contain a main image (although feel free to add more if you have anything suitable). I have included a picture in the dropbox folder titled "Front side image" which we would like used. I've also included in the folder an adobe image of grass which you may or may not like to use on either front or back.

Somewhere on both the front and back sides, you will need to include our contact details:
01632 960417
www.tavistrowgardening.co.uk/lawncare

The front side should show what treatments we currently have available. These are:

- Lawn Fertilising
- Scarification
- Aeration
- Weed Control
- Moss Control
- Hydration Booster
- PlumeRest
- Turfing & Renovation

"Select a one-off treatment or choose from one of our specially created lawn care packages."

BACK SIDE:
On the back, we will still need our logo and contact details but the image we'd like used should be the one in the dropbox folder titled "Back side image". Again, if you have any other images you feel would also work, then please feel free to add them.

The back side is to contain a bit more information and be a bit 'wordier' and so can you please include the following 2 paragraphs:

"As expert gardeners, we are passionate about horticulture and working to bring out the very best in your garden. When we work in your garden, we look at it and treat it with the same care and attention as if it were our own, before handing it back for you to enjoy. Our passion doesn't end at just trees and shrubs though. Your grass is as much of a living, breathing plant as your shrubs and we therefore utilise our expert horticultural knowledge to ensure your lawn thrives and reaches its fullest potential.

Lawn care isn't just about applying a fertiliser. It's about really understanding your lawn and being able to use extensive knowledge and experience to diagnose and treat issues. It therefore stands to reason that you should employ an expert to bring out the best in your lawn which is why we at Tavistrow Gardening Services have created a superior lawn care service that will keep your lawn looking lush, green and healthy all year round."

I referred at the very top of this brief to the fact we will need an infographic table created to show the different lawn care packages available. You see from the PDF table I created that we have 3 packages; Standard, Enhanced and Premium. Please create a visually appealing table which sets out the differences between our packages and include it on the back page.

Finally, somewhere we would like reference to the other gardening services we do. It's only to be something small as it isn't the main focus of the flyer but we think it would be good to mention what else we do. To re-iterate, it isnt to be big. I still want the main focus to be lawn care but if you could somehow reference that we also do the following services, that would be good. I will leave it to you to decide where on the flyer it fits in best, be it the front or back:

- Lawn mowing
- Shrub pruning
- Hedge trimming
- Weed killing
- Garden clearance & tidy-up
- Planting & design
- Regular Garden Maintenance
- Turfing
- Fencing
- Gutter clearance

I think thats it. I look forward to your designs!
Ps. Don't forget the dropbox folder:

Target Market(s)

Professional men/women aged 25+
Retired aged 65+

Industry/Entity Type

Home And Garden

Font styles to use
Sans Serif

Colors
6b449b
9bcb3c

Requirements
Must have
• Our company colours; purple and green; as per our website www.tavistrowgardening.co.uk. I've selected purple and green on this brief just to highlight the colours needed but please be sure to use the exact shades from our website and NOT the shade of purple and green that were selected on this brief.
• All the wording as explained in the main project brief.
Nice to have
• I want the flyer to be bold, eye-catching and modern.
• We particularly like the font Trebuchet MS for general copy but please feel free to use any other font for bolder, main titles.
Should not have
• We don't want anything gimmicky. No cheesy marketing.
• We only want professional looking designs. With the greatest of respect, if you're just starting out or don't really do design but think you'll use this as practise, please don't waste your or our time. We've previously run contests for other projects where we've had designs submitted that have clearly been done on MS Word and used Clipart and Wordart. That's really not what we are looking for.

```html
<!DOCTYPE html>
<html lang="en">
<head>
<meta charset="utf-8">
<title>Tavistrow Gardening Services – Lawn Treatment Flyer</title>
<link href="https://fonts.googleapis.com/css2?family=PT+Sans:wght@400;700&family=PT+Sans+Narrow:wght@400;700&display=swap" rel="stylesheet">
<style>
  :root{
    --violet:#6a4fd6;
    --violet-deep:#5a3fc4;
    --violet-row:#8b6ee0;
    --lime:#a8dc3a;
    --lime-row:#b9e545;
    --leaf:#8cc63f;
    --ink:#2e2a26;
    --brown:#3a2a22;
    --grey:#3c3c3c;
    --paper:#ffffff;
    --stage:#ece8e1;
  }
  *{box-sizing:border-box;margin:0;padding:0}
  html,body{width:1200px;height:877px;overflow:hidden}
  body{background:var(--stage);position:relative;font-family:"PT Sans",sans-serif;color:var(--ink)}

  .flyer{position:absolute;top:58px;height:764px;overflow:hidden;background:var(--paper);box-shadow:0 3px 10px rgba(0,0,0,.25)}
  .flyer--front{left:50px;width:533px}
  .flyer--back{left:620px;width:540px}

  .photo{position:absolute;left:0;top:0;width:100%}
  .photo--garden-path{height:420px;background:linear-gradient(180deg,#3c6a2a 0%,#5fae2e 18%,#7fcf2d 45%,#c7c1b4 60%,#6fc22a 75%,#5cae22 100%)}
  .photo--garden-path-full{height:100%;background:
      linear-gradient(115deg,transparent 45%,rgba(205,200,190,.85) 52%,rgba(205,200,190,.85) 60%,transparent 67%),
      linear-gradient(180deg,#3f6b2c 0%,#5faf2c 14%,#7ccd2c 40%,#6cbf26 75%,#5aa820 100%)}

  .flower-cluster{position:absolute;left:70px;top:175px;width:400px;height:160px;border-radius:50%;
      background:radial-gradient(ellipse at 55% 45%,#7a3f9a 0%,#8a5bb0 18%,#5fb830 45%,rgba(120,200,60,.6) 70%,rgba(120,200,60,0) 100%)}

  .panel-shape{position:absolute;left:0;top:0}

  .brand{position:absolute;display:flex;align-items:center;justify-content:center;gap:8px}
  .brand__dot{width:18px;height:18px;border-radius:50%;background:var(--leaf);flex:none}
  .brand__name{font-family:"PT Sans",sans-serif;font-weight:700;color:var(--brown);font-size:23px;line-height:1.1;text-align:center;white-space:nowrap}
  .flyer--front .brand{left:120px;top:350px;width:293px}
  .flyer--back .brand{left:30px;top:58px;width:240px;height:56px}
  .flyer--back .brand__name{font-size:21px}

  .strapline{position:absolute;left:0;top:418px;width:100%;text-align:center;color:var(--violet);
      font-family:"PT Sans",sans-serif;font-weight:700;font-size:30px;line-height:32px;letter-spacing:.2px}

  .grass-strip{position:absolute;left:0;top:490px;width:100%;height:66px;
      background:linear-gradient(180deg,rgba(140,210,50,0) 0%,#8fd43a 35%,#5fae1f 80%,#d8ecd0 100%)}

  .services{position:absolute;left:0;top:556px;width:100%;height:144px;background:linear-gradient(180deg,#f4f4f4,#ffffff)}
  .services__title{position:absolute;left:0;top:22px;width:100%;text-align:center;color:var(--leaf);
      font-weight:700;font-size:19px;font-variant:small-caps;letter-spacing:.3px}
  .services__list{position:absolute;left:86px;top:50px;width:400px;list-style:none;
      display:grid;grid-template-columns:172px 200px;row-gap:1px;font-weight:700;font-size:17.5px;color:var(--grey);grid-auto-flow:column;grid-template-rows:repeat(4,21.5px)}
  .services__list li{position:relative;padding-left:14px}
  .services__list li::before{content:"";position:absolute;left:0;top:8px;width:7px;height:7px;border-radius:50%;background:var(--leaf)}

  .contact{position:absolute;left:0;top:700px;width:100%;height:64px;text-align:center;font-weight:700}
  .contact--violet{background:var(--violet);color:#fff}
  .contact--lime{background:var(--lime);color:var(--ink)}
  .contact__phone{display:flex;align-items:center;justify-content:center;gap:6px;font-size:20px;padding-top:7px;letter-spacing:.5px}
  .contact__phone svg{width:20px;height:20px}
  .contact__web{font-size:17px;margin-top:1px}

  .about{position:absolute;left:28px;top:125px;width:252px;font-family:"PT Sans Narrow",sans-serif;font-size:12.7px;line-height:16.3px;color:#2b2b2b}
  .about p+p{margin-top:6px}

  .packages{position:absolute;left:28px;top:463px;width:484px;height:212px;border-radius:12px;background:rgba(235,230,250,.85);padding:5px 8px 0}
  .packages__title{text-align:center;font-weight:700;font-size:16px;color:var(--ink)}
  .packages table{width:100%;border-collapse:collapse;font-family:"PT Sans Narrow",sans-serif;font-weight:700;font-size:11.5px;margin-top:2px}
  .packages th{font-weight:700;text-align:center;height:18px;color:var(--ink)}
  .packages td{height:20.4px;text-align:center;color:var(--ink)}
  .packages td:first-child{text-align:left;padding-left:6px;width:143px}
  .packages td+td{border-left:1px solid rgba(255,255,255,.6)}
  .packages tr.row--violet td{background:var(--violet-row)}
  .packages tr.row--lime td{background:var(--lime-row)}
  .tick{font-size:15px;line-height:1}
</style>
</head>
<body>

<section class="flyer flyer--front">
  <div class="photo photo--garden-path" role="img" aria-label="Photograph of a winding stone path through lush green lawns"></div>
  <div class="flower-cluster" role="img" aria-label="Illustration of purple and white flowers with green leaves"></div>

  <svg class="panel-shape" width="533" height="764" viewBox="0 0 533 764" aria-hidden="true">
    <path d="M0,350 Q40,335 100,338 Q125,300 160,300 L373,300 Q408,300 433,338 Q493,335 533,350 L533,764 L0,764 Z" fill="#f2f2f4"/>
    <path d="M0,350 Q40,335 100,338 Q125,300 160,300 L373,300 Q408,300 433,338 Q493,335 533,350" fill="none" stroke="#6a4fd6" stroke-width="9"/>
  </svg>

  <div class="brand">
    <span class="brand__dot"></span>
    <span class="brand__name">Tavistrow Gardening<br>Services</span>
  </div>

  <h1 class="strapline">Lawn care by your local<br>gardening expert</h1>

  <div class="grass-strip" role="img" aria-label="Illustration of a strip of fresh grass blades"></div>

  <div class="services">
    <h2 class="services__title">Expert Lawn Treatment Services</h2>
    <ul class="services__list">
      <li>Lawn Fertilising</li>
      <li>Scarification</li>
      <li>Aeration</li>
      <li>Weed Control</li>
      <li>Moss Control</li>
      <li>Hydration Booster</li>
      <li>PlumeRest</li>
      <li>Turfing &amp; Renovation</li>
    </ul>
  </div>

  <footer class="contact contact--violet">
    <div class="contact__phone">
      <svg viewBox="0 0 20 20" aria-hidden="true"><circle cx="10" cy="10" r="8.5" fill="none" stroke="#fff" stroke-width="1.5"/><path d="M7 5.5c-.8.6-1.2 1.6-.8 3 .6 2.2 2.3 4.2 4.3 5.3 1.2.6 2.3.5 3-.2l.5-.6-1.8-1.6-1 .8c-1-.5-2-1.7-2.4-2.8l.9-.8L8.3 5z" fill="#fff"/></svg>
      01632 960417
    </div>
    <div class="contact__web">www.tavistrowgardening.co.uk/lawncare</div>
  </footer>
</section>

<section class="flyer flyer--back">
  <div class="photo photo--garden-path-full" role="img" aria-label="Photograph of a curving paved path through a manicured garden lawn"></div>

  <svg class="panel-shape" width="540" height="764" viewBox="0 0 540 764" aria-hidden="true">
    <path d="M28,12 L272,12 Q282,12 282,22 L282,428 Q282,440 294,440 L510,440 Q520,440 520,450 L520,680 Q520,690 510,690 L28,690 Q18,690 18,680 L18,22 Q18,12 28,12 Z" fill="rgba(255,255,255,.82)" stroke="#6a4fd6" stroke-width="2.5"/>
  </svg>

  <div class="brand">
    <span class="brand__dot"></span>
    <span class="brand__name">Tavistrow Gardening<br>Services</span>
  </div>

  <div class="about">
    <p>As expert gardeners, we are passionate about horticulture and working to bring out the very best in your garden. When we work in your garden, we look at it and treat it with the same care and attention as if it were our own, before handing it back for you to enjoy. Our passion doesn't end at just trees and shrubs though. Your grass is as much of a living, breathing plant as your shrubs and we therefore utilise our expert horticultural knowledge to ensure your lawn thrives and reaches its fullest potential.</p>
    <p>Lawn care isn't just about applying a fertiliser. It's about really understanding your lawn and being able to use extensive knowledge and experience to diagnose and treat issues. It therefore stands to reason that you should employ an expert to bring out the best in your lawn which is why we at Tavistrow Gardening Services have created a superior lawn care service that will keep your lawn looking lush, green and healthy all year round.</p>
  </div>

  <div class="packages">
    <h2 class="packages__title">Lawn Treatment Packages</h2>
    <table>
      <thead>
        <tr><th></th><th>Standard Package</th><th>Enhanced Package</th><th>Premium Package</th></tr>
      </thead>
      <tbody>
        <tr class="row--violet"><td>Spring Treatment</td><td class="tick">✓</td><td class="tick">✓</td><td class="tick">✓</td></tr>
        <tr class="row--lime"><td>Early Summer Treatment</td><td class="tick">✓</td><td class="tick">✓</td><td class="tick">✓</td></tr>
        <tr class="row--violet"><td>Late Summer Treatment</td><td class="tick">✓</td><td class="tick">✓</td><td class="tick">✓</td></tr>
        <tr class="row--lime"><td>Autumn/Winter Treatment</td><td class="tick">✓</td><td class="tick">✓</td><td class="tick">✓</td></tr>
        <tr class="row--violet"><td>Scarification</td><td></td><td class="tick">✓</td><td class="tick">✓</td></tr>
        <tr class="row--lime"><td>Aeration</td><td></td><td class="tick">✓</td><td class="tick">✓</td></tr>
        <tr class="row--violet"><td>PlumeRest Treatment</td><td></td><td></td><td class="tick">✓</td></tr>
        <tr class="row--lime"><td>Hydration Boost Treatment</td><td></td><td></td><td></td></tr>
      </tbody>
    </table>
  </div>

  <footer class="contact contact--lime">
    <div class="contact__phone">
      <svg viewBox="0 0 20 20" aria-hidden="true"><circle cx="10" cy="10" r="8.5" fill="none" stroke="#2e2a26" stroke-width="1.5"/><path d="M7 5.5c-.8.6-1.2 1.6-.8 3 .6 2.2 2.3 4.2 4.3 5.3 1.2.6 2.3.5 3-.2l.5-.6-1.8-1.6-1 .8c-1-.5-2-1.7-2.4-2.8l.9-.8L8.3 5z" fill="#2e2a26"/></svg>
      01632 960417
    </div>
    <div class="contact__web">www.tavistrowgardening.co.uk/lawncare</div>
  </footer>
</section>

</body>
</html>
```